RB Cargonet businesscard project

RB Cargonet Ltd is a freshly founded small (3 employees), young (average age is 30 years) company, living from the road transportation market without own tools.
We would like to have an impressive, new-line, cool busines card for a freshly founded forwarding company on an overcrowded market which raises attention and makes the potential partners eager to work with us.

Our logo is in the attachment, please use it for the card.

Target Market(s)

The main profile of the company is logistic/forwarding on road.

Industry/Entity Type

Freight Forwarding

Contact Information for Business Card

Name: Varga Edina
Title: general manager
mobile nr: +36-70/482-5910
fax nr: +36-1/655-3947
e-mail: edina.varga@rbcargonet-example.com
info@rbcargonet-example.com
website address: http://www.rbcargonet-example.com
and if possible maybe some funny or helpful info on the back

Requirements
Must have
• contact details above
Nice to have
• some really nice and catching back-side (info, graphics, useful tool info... anything)
Should not have
• trucks, road, ship, airplane on it...

```html
<!DOCTYPE html>
<html lang="en">
<head>
<meta charset="utf-8">
<title>RB Cargonet – Business Card</title>
<link rel="stylesheet" href="https://fonts.googleapis.com/css2?family=Open+Sans:wght@400;600;700&family=Oswald:wght@400&family=Merriweather:wght@900&display=swap">
<style>
  :root {
    --page-bg: #e9e7e4;
    --card-white: #ffffff;
    --card-black: #111214;
    --card-black-top: #2a2b2e;
    --ink-dark: #3b3b3d;
    --ink-mid: #555558;
    --brand-blue: #5b86c5;
    --brand-blue-light: #8fb0df;
    --divider: #d5d8de;
    --band-text: #ffffff;
  }
  * { margin: 0; padding: 0; box-sizing: border-box; }
  html, body { width: 1200px; height: 913px; overflow: hidden; }
  body {
    background: var(--page-bg);
    font-family: "Open Sans", Arial, sans-serif;
    position: relative;
  }
  .card {
    position: absolute;
    width: 560px;
    height: 320px;
    border-radius: 18px;
    overflow: hidden;
    box-shadow: 0 10px 28px rgba(0,0,0,.22);
  }
  /* Front */
  .card-front {
    left: 60px; top: 80px;
    background: var(--card-white);
  }
  .front-brand {
    position: absolute;
    left: 40px; top: 0; bottom: 0;
    width: 230px;
    display: flex; align-items: center; gap: 12px;
  }
  .brand-square {
    width: 26px; height: 26px;
    background: var(--brand-blue);
    flex: none;
  }
  .brand-name {
    font-family: "Oswald", "Arial Narrow", sans-serif;
    font-size: 40px;
    color: var(--ink-dark);
    line-height: 1;
    white-space: nowrap;
  }
  .front-divider {
    position: absolute;
    left: 282px; top: 60px; bottom: 60px;
    width: 1px;
    background: var(--divider);
  }
  .front-details {
    position: absolute;
    left: 302px; top: 82px;
    right: 18px;
  }
  .person-name {
    font-weight: 700;
    font-size: 21px;
    color: var(--ink-mid);
    line-height: 1.1;
  }
  .person-title {
    font-size: 14px;
    color: var(--brand-blue);
    margin-bottom: 14px;
  }
  .contact-list { list-style: none; }
  .contact-list li {
    display: flex; align-items: center; gap: 8px;
    font-size: 12.5px;
    color: var(--ink-dark);
    line-height: 21px;
    white-space: nowrap;
  }
  .contact-list svg {
    width: 12px; height: 12px; flex: none;
    fill: none; stroke: var(--brand-blue); stroke-width: 1.6;
  }
  /* Back */
  .card-back {
    left: 580px; top: 500px;
    background: linear-gradient(160deg, var(--card-black-top) 0%, var(--card-black) 60%);
  }
  .back-brand {
    position: absolute;
    left: 0; right: 0; top: 78px;
    display: flex; justify-content: center; align-items: center; gap: 14px;
  }
  .back-brand .brand-name { color: #ffffff; font-size: 46px; }
  .back-email {
    position: absolute;
    left: 0; right: 0; top: 150px;
    text-align: center;
    font-size: 15px;
    color: var(--brand-blue-light);
  }
  .back-band {
    position: absolute;
    left: 0; right: 0; bottom: 70px;
    height: 38px;
    background: linear-gradient(90deg, var(--brand-blue) 0%, var(--brand-blue-light) 75%, #b9c6d8 100%);
    display: flex; align-items: center; justify-content: center;
  }
  .back-tagline {
    font-family: "Merriweather", Georgia, serif;
    font-weight: 900;
    font-size: 14px;
    letter-spacing: .5px;
    color: var(--band-text);
  }
</style>
</head>
<body>

  <section class="card card-front" aria-label="Business card front">
    <div class="front-brand">
      <span class="brand-square"></span>
      <span class="brand-name">RB Cargonet</span>
    </div>
    <div class="front-divider"></div>
    <div class="front-details">
      <p class="person-name">Varga Edina</p>
      <p class="person-title">General Manager</p>
      <ul class="contact-list">
        <li>
          <svg viewBox="0 0 12 12"><rect x="3" y="0.8" width="6" height="10.4" rx="1"/><line x1="5" y1="9.3" x2="7" y2="9.3"/></svg>
          +36-70/482-5910
        </li>
        <li>
          <svg viewBox="0 0 12 12"><rect x="1" y="4.5" width="10" height="6.5" rx="1"/><rect x="3" y="1" width="6" height="3.5"/></svg>
          +36-1/655-3947
        </li>
        <li>
          <svg viewBox="0 0 12 12"><circle cx="6" cy="6" r="5"/><ellipse cx="6" cy="6" rx="2.2" ry="5"/><line x1="1" y1="6" x2="11" y2="6"/></svg>
          www.rbcargonet-example.com
        </li>
        <li>
          <svg viewBox="0 0 12 12"><rect x="0.8" y="2.5" width="10.4" height="7.5"/><polyline points="0.8,2.5 6,6.8 11.2,2.5"/></svg>
          edina.varga@rbcargonet-example.com
        </li>
      </ul>
    </div>
  </section>

  <section class="card card-back" aria-label="Business card back">
    <div class="back-brand">
      <span class="brand-square"></span>
      <span class="brand-name">RB Cargonet</span>
    </div>
    <p class="back-email">info@rbcargonet-example.com</p>
    <div class="back-band">
      <p class="back-tagline">THAT IS COOL IF YOU ARE HERE</p>
    </div>
  </section>

</body>
</html>
```